Sales and Lettings Boards

Hello, please see attached our sales and lettings boards for our estate agency. These were "designed" by the sign writers. As you can see they are pretty flat and boring - could you work your magic and make them stand out please? I've also attached the logo files. Many thanks, Glen

Target Market(s)

Consumers - residential sale property sales and lettings

Industry/Entity Type

Real Estate Agent

```html
<!DOCTYPE html>
<html lang="en">
<head>
<meta charset="utf-8">
<title>Harben Sales &amp; Lettings – Property Boards</title>
<link rel="stylesheet" href="https://fonts.googleapis.com/css2?family=Roboto:wght@500;700;900&family=Oswald:wght@500;600&display=swap">
<style>
  :root {
    --ink: #525254;
    --green: #66bb4c;
    --white: #ffffff;
    --frame: #e6e7e9;
    --edge: #9a9a9a;
  }
  * { margin: 0; padding: 0; box-sizing: border-box; }
  html, body { width: 1200px; height: 1200px; overflow: hidden; background: var(--white); }
  .canvas {
    position: relative;
    width: 1200px;
    height: 1200px;
    background: var(--white);
    border: 2px solid var(--frame);
  }
  .frame {
    position: absolute;
    left: 40px; top: 40px;
    width: 1120px; height: 1120px;
    border: 14px solid var(--frame);
  }
  .brand {
    position: absolute;
    left: 0; right: 0; top: 262px;
    text-align: center;
    color: var(--ink);
    font-family: "Roboto", Arial, sans-serif;
  }
  .brand-name {
    font-size: 118px;
    font-weight: 700;
    line-height: 1;
    letter-spacing: 2px;
  }
  .brand-tagline {
    margin-top: 30px;
    font-size: 52px;
    font-weight: 700;
    line-height: 1;
  }
  .brand-tagline .amp { color: var(--green); }
  .boards {
    position: absolute;
    top: 521px;
    left: 0; right: 0;
  }
  .board {
    position: absolute;
    top: 0;
    width: 274px;
    height: 381px;
    overflow: visible;
  }
  .board--sale { left: 142px; }
  .board--rooms { left: 458px; }
  .board--let { left: 784px; }
  .board .outline { fill: var(--white); stroke: var(--edge); stroke-width: 1; }
  .board .band-green { fill: var(--green); }
  .board .band-dark { fill: var(--ink); }
  .board .emblem { fill: var(--ink); stroke: var(--white); stroke-width: 6; }
  .board .rule { stroke: var(--green); stroke-width: 2; }
  .board .name { font-family: "Roboto", Arial, sans-serif; font-weight: 700; font-size: 38px; fill: var(--ink); }
  .board .tagline { font-family: "Roboto", Arial, sans-serif; font-weight: 500; font-size: 20px; fill: var(--ink); }
  .board .tagline .amp { fill: var(--green); }
  .board .phone { font-family: "Oswald", "Arial Narrow", sans-serif; font-weight: 500; font-size: 38px; fill: var(--white); }
  .board .web { font-family: "Roboto", Arial, sans-serif; font-weight: 500; font-size: 14.5px; fill: var(--green); }
  .board .status { font-family: "Roboto", Arial, sans-serif; font-weight: 900; font-size: 40px; fill: var(--white); }
  .board .status--narrow { font-family: "Oswald", "Arial Narrow", sans-serif; font-weight: 600; font-size: 38px; }
</style>
</head>
<body>
<main class="canvas">
  <div class="frame"></div>

  <header class="brand">
    <div class="brand-name">HARBEN</div>
    <div class="brand-tagline">Sales <span class="amp">&amp;</span> Lettings</div>
  </header>

  <section class="boards">
    <svg class="board board--sale" viewBox="0 0 274 381" aria-label="For sale board">
      <path class="outline" d="M0.5,50 H68.4 A72,72 0 0 1 205.6,50 H273.5 V380.5 H0.5 Z"/>
      <rect class="band-green" x="8" y="61" width="258" height="57"/>
      <circle class="emblem" cx="137" cy="72" r="64"/>
      <text class="name" x="137" y="190" text-anchor="middle">HARBEN</text>
      <text class="tagline" x="137" y="217" text-anchor="middle">Sales <tspan class="amp">&amp;</tspan> Lettings</text>
      <rect class="band-dark" x="0.5" y="233" width="273" height="77"/>
      <text class="phone" x="137" y="282" text-anchor="middle">01632 960418</text>
      <line class="rule" x1="22" y1="291" x2="252" y2="291"/>
      <text class="web" x="137" y="305" text-anchor="middle">www.harben-estates.co.uk</text>
      <rect class="band-green" x="0.5" y="312" width="273" height="68.5"/>
      <text class="status" x="137" y="361" text-anchor="middle">FOR SALE</text>
    </svg>

    <svg class="board board--rooms" viewBox="0 0 274 381" aria-label="Rooms to let board">
      <path class="outline" d="M0.5,50 H68.4 A72,72 0 0 1 205.6,50 H273.5 V380.5 H0.5 Z"/>
      <rect class="band-green" x="8" y="61" width="258" height="57"/>
      <circle class="emblem" cx="137" cy="72" r="64"/>
      <text class="name" x="137" y="190" text-anchor="middle">HARBEN</text>
      <text class="tagline" x="137" y="217" text-anchor="middle">Sales <tspan class="amp">&amp;</tspan> Lettings</text>
      <rect class="band-dark" x="0.5" y="233" width="273" height="77"/>
      <text class="phone" x="137" y="282" text-anchor="middle">01632 960418</text>
      <line class="rule" x1="22" y1="291" x2="252" y2="291"/>
      <text class="web" x="137" y="305" text-anchor="middle">www.harben-estates.co.uk</text>
      <rect class="band-green" x="0.5" y="312" width="273" height="68.5"/>
      <text class="status status--narrow" x="137" y="361" text-anchor="middle">ROOMS TO LET</text>
    </svg>

    <svg class="board board--let" viewBox="0 0 274 381" aria-label="To let board">
      <path class="outline" d="M0.5,50 H68.4 A72,72 0 0 1 205.6,50 H273.5 V380.5 H0.5 Z"/>
      <rect class="band-green" x="8" y="61" width="258" height="57"/>
      <circle class="emblem" cx="137" cy="72" r="64"/>
      <text class="name" x="137" y="190" text-anchor="middle">HARBEN</text>
      <text class="tagline" x="137" y="217" text-anchor="middle">Sales <tspan class="amp">&amp;</tspan> Lettings</text>
      <rect class="band-dark" x="0.5" y="233" width="273" height="77"/>
      <text class="phone" x="137" y="282" text-anchor="middle">01632 960418</text>
      <line class="rule" x1="22" y1="291" x2="252" y2="291"/>
      <text class="web" x="137" y="305" text-anchor="middle">www.harben-estates.co.uk</text>
      <rect class="band-green" x="0.5" y="312" width="273" height="68.5"/>
      <text class="status" x="137" y="361" text-anchor="middle">TO LET</text>
    </svg>
  </section>
</main>
</body>
</html>
```